Business Card

I need a business card that really pops for a potential customer or person who refers a personal injury lead. I want to highlight our office locations, but only address that needs to be on the card is my office's main address. I want a sleek, modern and minimalist design.

```html
<!DOCTYPE html>
<html lang="en">
<head>
<meta charset="utf-8">
<title>Prairie Injury Lawyers – Business Card</title>
<link rel="stylesheet" href="https://fonts.googleapis.com/css2?family=Arimo:wght@400&family=Jost:wght@400;500&display=swap">
<style>
  :root {
    --page-bg: #e6e6e8;
    --card-bg: #f3f3f4;
    --ink: #3c3c3e;
    --ink-soft: #4a4a4c;
    --rule: #5a5a5c;
  }
  * { margin: 0; padding: 0; box-sizing: border-box; }
  html, body {
    width: 1200px;
    height: 1140px;
    overflow: hidden;
    background: var(--page-bg);
  }
  .canvas {
    position: relative;
    width: 1200px;
    height: 1140px;
  }
  .business-card {
    position: absolute;
    left: 75px;
    top: 270px;
    width: 1050px;
    height: 600px;
    background: var(--card-bg);
    border-radius: 26px;
    box-shadow: 0 10px 30px rgba(0,0,0,0.12);
    color: var(--ink);
  }
  .office-address {
    position: absolute;
    left: 98px;
    top: 92px;
    font-family: "Arimo", Helvetica, Arial, sans-serif;
    font-size: 25px;
    line-height: 35px;
    font-style: normal;
    color: var(--ink-soft);
  }
  .firm-name {
    position: absolute;
    right: 96px;
    top: 106px;
    text-align: right;
    font-family: "Arimo", Helvetica, Arial, sans-serif;
    font-weight: 400;
    font-size: 32px;
    line-height: 40px;
    color: var(--ink);
  }
  .website-row {
    position: absolute;
    left: 98px;
    right: 96px;
    top: 298px;
    display: flex;
    align-items: center;
    gap: 24px;
  }
  .website-row__rule {
    flex: 1;
    height: 2px;
    background: var(--rule);
  }
  .website-row__url {
    font-family: "Arimo", Helvetica, Arial, sans-serif;
    font-size: 24px;
    letter-spacing: 4.2px;
    color: var(--ink-soft);
  }
  .attorney {
    position: absolute;
    left: 98px;
    top: 440px;
    font-family: "Jost", "Futura", sans-serif;
  }
  .attorney__name {
    font-weight: 500;
    font-size: 44px;
    line-height: 46px;
    letter-spacing: -1px;
    color: var(--ink);
  }
  .attorney__title {
    font-weight: 400;
    font-size: 25px;
    line-height: 30px;
    letter-spacing: 9px;
    color: var(--ink);
  }
  .contact-details {
    position: absolute;
    left: 568px;
    top: 458px;
    font-family: "Arimo", Helvetica, Arial, sans-serif;
    font-size: 25px;
    line-height: 35px;
    color: var(--ink-soft);
  }
</style>
</head>
<body>
  <div class="canvas">
    <section class="business-card">
      <address class="office-address">
        270 West Harbor Avenue<br>
        Suite 1810<br>
        Chicago, IL 60611
      </address>

      <div class="firm-name">Prairie Injury Lawyers</div>

      <div class="website-row">
        <span class="website-row__rule"></span>
        <span class="website-row__url">www.prairieinjurylawyers.com</span>
        <span class="website-row__rule"></span>
      </div>

      <div class="attorney">
        <div class="attorney__name">DORIAN KESSLER</div>
        <div class="attorney__title">ATTORNEY</div>
      </div>

      <div class="contact-details">
        <div class="contact-details__phone">312-555-0147</div>
        <div class="contact-details__email">info@prairieinjurylawyers.com</div>
      </div>
    </section>
  </div>
</body>
</html>
```